Business card and stationary for LOGISTICS company | ||
HAULVEX 514K | ||
Use same font as used in my logo | ||
Corporate Modern Professional Simple |
Oleksa | ||
Air and Sea freight from China to Ukraine | ||
Beijing, Lunmao Plaza C4-517K | ||
beijing@haulvex514k.com | ||
www.haulvex514k.com | ||
skype: mvoloshenko | ||
This business card would be given to the new registered client. After registration client receives his own client-number for air and for sea freight. I would need 2 lines on the back with plane and boat logo in front on it so I can write the clients number | ||

```html
<!DOCTYPE html>
<html lang="en">
<head>
<meta charset="utf-8">
<title>HAULVEX 514K — Stationery</title>
<link href="https://fonts.googleapis.com/css2?family=Montserrat:wght@500;700;800&family=Open+Sans:wght@400;600;700&display=swap" rel="stylesheet">
<style>
:root{
  --bg:#2b2b2b;
  --paper:#ffffff;
  --red:#e3202a;
  --yellow:#f6c500;
  --blue:#1f7ac2;
  --ink:#3a3a3a;
  --muted:#8a8a8a;
  --rule:#9a9a9a;
}
*{box-sizing:border-box;margin:0;padding:0}
html,body{width:1200px;height:754px;overflow:hidden;background:var(--bg)}
body{position:relative;font-family:"Open Sans",Arial,sans-serif;color:var(--ink)}
.piece{position:absolute;background:var(--paper);overflow:hidden;box-shadow:0 6px 18px rgba(0,0,0,.45)}
.logo{position:absolute;display:flex;align-items:center;gap:5px;font-family:"Montserrat",Arial,sans-serif;font-weight:800;color:var(--red);letter-spacing:.5px;white-space:nowrap}
.logo .dot{width:1em;height:1em;border-radius:50%;background:var(--red)}
.contact{position:absolute;text-align:right;font-size:6px;line-height:1.5;color:var(--muted);white-space:nowrap}
.band{position:absolute;left:0;right:0;bottom:0;height:14px;border-top:4px solid var(--yellow);background:var(--paper)}
.band .tab{position:absolute;right:0;top:0;bottom:0;width:36%;background:var(--blue);color:#fff;font-size:6px;font-weight:600;display:flex;align-items:center;justify-content:center;white-space:nowrap}
.tagline{position:absolute;font-size:7px;font-weight:600;color:var(--red);white-space:nowrap}

/* fax */
.fax{left:40px;top:40px;width:300px;height:424px}
.fax .title{position:absolute;right:22px;top:62px;font-family:"Montserrat",sans-serif;font-weight:800;font-size:13px;color:var(--ink)}
.fax table{position:absolute;left:22px;top:84px;width:256px;border-collapse:collapse;font-size:6px;color:var(--muted)}
.fax td{border:0.8px solid var(--rule);height:16px;padding:2px 4px;vertical-align:top}

/* letterhead */
.letter{left:370px;top:40px;width:300px;height:424px}

/* envelope */
.envelope{left:700px;top:40px;width:460px;height:230px}
.envelope .flap{position:absolute;inset:0}

/* slip */
.slip{left:700px;top:300px;width:460px;height:164px}

/* cards */
.card{top:510px;width:350px;height:200px;border-radius:8px}
.card-back{left:40px}
.card-front{left:425px}
.card-alt{left:810px}
.numline{position:absolute;left:30px;right:30px;display:flex;align-items:flex-end;gap:10px;font-size:8px;color:var(--muted)}
.numline svg{flex:none}
.numline .label{width:34px}
.numline .line{flex:1;border-bottom:1px solid var(--rule);height:18px}
.card-front .panel{position:absolute;left:0;right:0;bottom:0;height:112px;background:var(--blue);border-top:6px solid var(--yellow)}
.name{position:absolute;font-family:"Montserrat",sans-serif;font-weight:800;white-space:nowrap}
.role{position:absolute;font-size:7px;white-space:nowrap;text-align:right}
.details{position:absolute;font-size:8px;line-height:1.7;white-space:nowrap}
</style>
</head>
<body>

<section class="piece fax">
  <div class="logo" style="left:22px;top:22px;font-size:13px"><span class="dot"></span>HAULVEX 514K</div>
  <div class="contact" style="right:22px;top:22px">Beijing, Lunmao Plaza C4-517K<br>beijing@haulvex514k.com<br>www.haulvex514k.com</div>
  <div class="title">FAX</div>
  <table>
    <tr><td>To</td><td>From</td></tr>
    <tr><td>Fax</td><td>Pages</td></tr>
    <tr><td>Date</td><td>Re</td></tr>
  </table>
  <div class="tagline" style="left:22px;bottom:24px">Air and Sea freight from China to Ukraine</div>
  <div class="band"><div class="tab">www.haulvex514k.com</div></div>
</section>

<section class="piece letter">
  <div class="logo" style="left:22px;top:22px;font-size:13px"><span class="dot"></span>HAULVEX 514K</div>
  <div class="contact" style="right:22px;top:22px">Beijing, Lunmao Plaza C4-517K<br>beijing@haulvex514k.com<br>skype: haulvex.oleksa</div>
  <div class="tagline" style="left:22px;bottom:24px">Air and Sea freight from China to Ukraine</div>
  <div class="band"><div class="tab">www.haulvex514k.com</div></div>
</section>

<section class="piece envelope">
  <svg class="flap" width="460" height="230" viewBox="0 0 460 230" aria-hidden="true">
    <polyline points="0,0 230,118 460,0" fill="none" stroke="#dcdcdc" stroke-width="1.5"/>
  </svg>
  <div class="logo" style="left:196px;top:132px;font-size:12px"><span class="dot"></span>HAULVEX 514K</div>
  <div class="band"><div class="tab">www.haulvex514k.com</div></div>
</section>

<section class="piece slip">
  <div class="logo" style="left:22px;top:20px;font-size:14px"><span class="dot"></span>HAULVEX 514K</div>
  <div class="tagline" style="left:22px;top:64px;font-size:8px">Air and Sea freight from China to Ukraine</div>
  <div class="band"><div class="tab">www.haulvex514k.com</div></div>
</section>

<section class="piece card card-back">
  <div class="logo" style="left:30px;top:24px;font-size:13px"><span class="dot"></span>HAULVEX 514K</div>
  <div class="numline" style="top:78px">
    <svg width="22" height="22" viewBox="0 0 24 24" aria-label="Air freight"><path fill="#1f7ac2" d="M21 16v-2l-8-5V3.5a1.5 1.5 0 0 0-3 0V9l-8 5v2l8-2.5V19l-2 1.5V22l3.5-1 3.5 1v-1.5L13 19v-5.5z"/></svg>
    <span class="label">Air No.</span><span class="line"></span>
  </div>
  <div class="numline" style="top:120px">
    <svg width="22" height="22" viewBox="0 0 24 24" aria-label="Sea freight"><path fill="#1f7ac2" d="M3 14h18l-3 6H6zM6 13V9h12v4zM10 8V4h4v4z"/></svg>
    <span class="label">Sea No.</span><span class="line"></span>
  </div>
  <div class="band"><div class="tab">www.haulvex514k.com</div></div>
</section>

<section class="piece card card-front">
  <div class="logo" style="left:24px;top:28px;font-size:18px"><span class="dot"></span>HAULVEX 514K</div>
  <div class="panel">
    <div class="name" style="right:20px;top:12px;font-size:20px;color:var(--yellow)">Oleksa</div>
    <div class="role" style="right:20px;top:40px;color:#fff">Sales Manager</div>
    <div class="details" style="left:20px;top:14px;color:#fff">Beijing, Lunmao Plaza C4-517K<br>beijing@haulvex514k.com<br>www.haulvex514k.com<br>skype: haulvex.oleksa</div>
  </div>
</section>

<section class="piece card card-alt">
  <div class="logo" style="left:24px;top:22px;font-size:14px"><span class="dot"></span>HAULVEX 514K</div>
  <div class="name" style="right:22px;top:62px;font-size:18px;color:var(--red)">Oleksa</div>
  <div class="role" style="right:22px;top:88px;color:var(--muted)">Air and Sea freight<br>from China to Ukraine</div>
  <div class="details" style="left:24px;top:82px;color:var(--ink)">Beijing, Lunmao Plaza C4-517K<br>beijing@haulvex514k.com<br>skype: haulvex.oleksa</div>
  <div class="band"><div class="tab">www.haulvex514k.com</div></div>
</section>

</body>
</html>
```